Marlow Sky Charter E-mail Signature

Need to create an email signature for Marlow Sky Charter. Signature should include the Marlow logo and the associated QFTR member logo

```html
<!DOCTYPE html>
<html lang="en">
<head>
<meta charset="utf-8">
<title>Marlow Sky Charter – Email Signature</title>
<link rel="stylesheet" href="https://fonts.googleapis.com/css2?family=PT+Sans:wght@400;700&display=swap">
<style>
  :root {
    --backdrop: #6ecff4;
    --card: #ffffff;
    --ink: #1e1e1e;
    --brand-blue: #2a6bb5;
    --rule: #262626;
  }
  * { margin: 0; padding: 0; box-sizing: border-box; }
  html, body {
    width: 1200px;
    height: 496px;
    overflow: hidden;
    background: var(--backdrop);
    font-family: "PT Sans", sans-serif;
  }
  .signature {
    position: absolute;
    left: 84px;
    top: 77px;
    width: 1027px;
    height: 330px;
    background: var(--card);
    box-shadow: 0 2px 6px rgba(0, 0, 0, 0.25);
  }
  .person-name {
    position: absolute;
    left: 33px;
    top: 20px;
    font-size: 76px;
    font-weight: 400;
    line-height: 1;
    color: var(--ink);
    letter-spacing: 0.5px;
  }
  .person-title {
    position: absolute;
    left: 36px;
    top: 99px;
    font-size: 45px;
    font-weight: 400;
    line-height: 1;
    color: var(--brand-blue);
  }
  .divider {
    position: absolute;
    left: 30px;
    top: 166px;
    width: 847px;
    height: 2px;
    background: var(--rule);
  }
  .membership {
    position: absolute;
    left: 41px;
    top: 224px;
    display: flex;
    align-items: center;
    gap: 12px;
  }
  .membership-badge {
    width: 50px;
    height: 35px;
    border-radius: 50%;
    background: var(--brand-blue);
  }
  .membership-text {
    display: flex;
    flex-direction: column;
    color: var(--ink);
    line-height: 1;
  }
  .membership-label {
    font-size: 12px;
    margin-bottom: 4px;
  }
  .membership-name {
    font-size: 28px;
    letter-spacing: 5px;
  }
  .brand {
    position: absolute;
    right: 67px;
    top: 196px;
    text-align: left;
    color: var(--brand-blue);
    font-weight: 700;
    line-height: 1;
    text-transform: uppercase;
  }
  .brand-main {
    display: block;
    font-size: 74px;
    letter-spacing: 6px;
  }
  .brand-sub {
    display: block;
    margin-top: 6px;
    font-size: 31px;
    letter-spacing: 6.5px;
  }
</style>
</head>
<body>
  <section class="signature">
    <h1 class="person-name">LOREM IPSUM</h1>
    <p class="person-title">Designation</p>
    <div class="divider"></div>

    <div class="membership">
      <div class="membership-badge"></div>
      <div class="membership-text">
        <span class="membership-label">member of</span>
        <span class="membership-name">QFTR</span>
      </div>
    </div>

    <div class="brand">
      <span class="brand-main">Marlow</span>
      <span class="brand-sub">Sky Charter</span>
    </div>
  </section>
</body>
</html>
```